Design NEW business card

We would like a business card using the colour deep red wine or dark navy blue textured background (patterned or not, open to suggestions) with a high gloss debossed rose gold/copper TM Thomas Marlow Jewellery business name (Provided). I have included images for your review we would like to keep our currently logo and business name on the front but you can change the layout and positioning. For the back of the card we are open to all suggestions/variations.
Use our current TM Thomas Marlow Jewellery logo (Provided image)

```html
<!DOCTYPE html>
<html lang="en">
<head>
<meta charset="utf-8">
<title>Thomas Marlow Jewellery – Business Card</title>
<link href="https://fonts.googleapis.com/css2?family=Josefin+Sans:wght@300;400&family=Montserrat:wght@400;500;600&display=swap" rel="stylesheet">
<style>
  :root {
    --backdrop: #ececec;
    --wine-dark: #3a1012;
    --wine: #4e1a1c;
    --wine-light: #5a2224;
    --onyx-dark: #141414;
    --onyx: #232323;
    --onyx-light: #2e2e2e;
    --rose-gold: #c48a64;
    --rose-gold-soft: #b5805f;
  }
  * { margin: 0; padding: 0; box-sizing: border-box; }
  html, body {
    width: 1200px;
    height: 803px;
    overflow: hidden;
    background: var(--backdrop);
  }
  .canvas {
    position: relative;
    width: 1200px;
    height: 803px;
  }
  .card {
    position: absolute;
    width: 540px;
    height: 310px;
    border-radius: 34px;
    overflow: hidden;
    box-shadow: 0 14px 30px rgba(0,0,0,0.18);
  }
  .card-texture {
    position: absolute;
    inset: 0;
  }

  /* Front: wine card with business name */
  .card-front {
    left: 80px;
    top: 430px;
  }
  .card-front .card-texture {
    background: radial-gradient(ellipse at 35% 40%, var(--wine-light), var(--wine) 55%, var(--wine-dark));
  }
  .brand {
    position: absolute;
    right: 52px;
    top: 128px;
    text-align: center;
    font-family: "Josefin Sans", sans-serif;
    font-weight: 300;
    color: var(--rose-gold);
  }
  .brand-name {
    font-size: 30px;
    letter-spacing: 7px;
    white-space: nowrap;
  }
  .brand-line {
    margin-top: 4px;
    font-size: 13px;
    letter-spacing: 14px;
    padding-left: 14px;
  }

  /* Back: onyx card with contact details */
  .card-back {
    left: 600px;
    top: 100px;
  }
  .card-back .card-texture {
    background: linear-gradient(135deg, var(--onyx-light), var(--onyx) 50%, var(--onyx-dark));
  }
  .person {
    position: absolute;
    left: 44px;
    bottom: 70px;
    font-family: "Montserrat", sans-serif;
    color: var(--rose-gold);
  }
  .person-name {
    font-size: 22px;
    font-weight: 500;
    letter-spacing: 1.5px;
  }
  .person-role {
    margin-top: 4px;
    font-size: 12px;
    font-weight: 400;
    letter-spacing: 1.2px;
    color: var(--rose-gold-soft);
  }
  .contact {
    position: absolute;
    right: 40px;
    top: 120px;
    font-family: "Montserrat", sans-serif;
    font-size: 11px;
    letter-spacing: 1.3px;
    line-height: 1.55;
    color: var(--rose-gold);
  }
  .contact-web {
    margin-top: 14px;
  }
</style>
</head>
<body>
<main class="canvas">

  <section class="card card-front" aria-label="Card front">
    <div class="card-texture" role="img" aria-label="Deep wine red fibrous paper texture"></div>
    <div class="brand">
      <div class="brand-name">THOMAS MARLOW</div>
      <div class="brand-line">JEWELLERY</div>
    </div>
  </section>

  <section class="card card-back" aria-label="Card back">
    <div class="card-texture" role="img" aria-label="Black card with subtle tone-on-tone geometric diamond pattern"></div>
    <div class="contact">
      <div class="contact-email">DANIEL@MARLOWJEWELLERY.COM</div>
      <div class="contact-phone">+91 900-555-0142</div>
      <div class="contact-web">WWW.MARLOWJEWELLERY.COM</div>
    </div>
    <div class="person">
      <div class="person-name">DANIEL WHITFORD</div>
      <div class="person-role">CO-FOUNDER &amp; CEO</div>
    </div>
  </section>

</main>
</body>
</html>
```